Chatterly Design Project

I need new cover graphics for my father's chatterly page. He is running for major of our town in Puerto Rico.
Need his name on the cover: Mateo Quiñones
And the position, town and year: Alcalde Carolina 2012
As a default background color you can use the blue in the current cover graphic, or go here for color ideas http://www.adelantevecinos2012.com/indexContinuar.php
I really would like to see something that incorporates some of the pictures I have uploaded of him with people in the town, or with popular leaders. He is the guy with gray hair.
Below is the target chatterly page. Thanks
https://www.chatterly.com/mateoquinones.valderrama
Town

```html
<!DOCTYPE html>
<html lang="es">
<head>
<meta charset="utf-8">
<title>Mateo Quiñones — Alcalde Carolina 2012</title>
<link rel="stylesheet" href="https://fonts.googleapis.com/css2?family=Cookie&family=Fira+Sans:wght@500&display=swap">
<style>
  :root {
    --sky-deep: #1ea6dc;
    --sky-mid: #4fc3ee;
    --sky-light: #a9e3f8;
    --cloud: rgba(255, 255, 255, 0.55);
    --band-blue: #243f8f;
    --band-red: #e41b23;
    --band-red-dark: #b3141b;
    --ink-white: #ffffff;
    --portrait-light: #e9e3de;
    --portrait-mid: #b9aaa0;
    --portrait-dark: #6d7da6;
  }
  html, body {
    margin: 0;
    padding: 0;
    overflow: hidden;
    background: #ffffff;
  }
  .cover {
    position: relative;
    width: 1200px;
    height: 444px;
    overflow: hidden;
    background:
      radial-gradient(ellipse 260px 90px at 330px 110px, var(--cloud), transparent 70%),
      radial-gradient(ellipse 300px 80px at 700px 330px, rgba(255,255,255,0.35), transparent 70%),
      radial-gradient(ellipse 220px 70px at 120px 380px, rgba(255,255,255,0.4), transparent 70%),
      radial-gradient(ellipse 240px 90px at 980px 60px, rgba(255,255,255,0.45), transparent 70%),
      linear-gradient(160deg, var(--sky-mid) 0%, var(--sky-deep) 45%, var(--sky-light) 100%);
  }
  .ribbon {
    position: absolute;
    left: 0;
    top: 193px;
    width: 1200px;
    height: 88px;
  }
  .candidate-name {
    position: absolute;
    left: 0;
    width: 1080px;
    margin: 0;
    text-align: center;
    font-family: "Cookie", cursive;
    font-weight: 400;
    font-size: 200px;
    color: var(--ink-white);
    text-shadow: 2px 4px 6px rgba(0, 40, 90, 0.45);
    line-height: 1;
    white-space: nowrap;
  }
  .candidate-name--first { top: 18px; }
  .candidate-name--last { top: 272px; }
  .office-line {
    position: absolute;
    left: 300px;
    width: 530px;
    top: 193px;
    height: 88px;
    margin: 0;
    display: flex;
    align-items: center;
    justify-content: center;
    font-family: "Fira Sans", sans-serif;
    font-weight: 500;
    font-size: 36px;
    line-height: 1;
    letter-spacing: 0.5px;
    color: var(--ink-white);
    white-space: nowrap;
  }
  .portrait {
    position: absolute;
    left: 800px;
    top: 46px;
    width: 400px;
    height: 398px;
    background:
      radial-gradient(ellipse 120px 150px at 190px 150px, var(--portrait-light), var(--portrait-mid) 70%, transparent 100%),
      linear-gradient(180deg, transparent 55%, var(--portrait-dark) 100%);
    -webkit-mask-image: radial-gradient(ellipse 200px 230px at 200px 210px, #000 70%, transparent 100%);
    mask-image: radial-gradient(ellipse 200px 230px at 200px 210px, #000 70%, transparent 100%);
  }
</style>
</head>
<body>
  <main class="cover">
    <svg class="ribbon" viewBox="0 0 1200 88" width="1200" height="88" aria-hidden="true">
      <polygon points="0,0 290,0 315,44 290,88 0,88" fill="var(--band-blue)"/>
      <polygon points="258,0 1200,0 1200,88 258,88 286,44" fill="var(--band-red)"/>
      <rect x="1130" y="0" width="70" height="88" fill="var(--band-red-dark)"/>
    </svg>

    <h1 class="candidate-name candidate-name--first">Mateo</h1>
    <p class="office-line">ALCALDE | CAROLINA | 2012</p>
    <p class="candidate-name candidate-name--last">Quiñones</p>

    <div class="portrait" role="img" aria-label="Portrait photo of the candidate, a gray-haired man in a striped shirt"></div>
  </main>
</body>
</html>
```